Card design for orthopaedic surgeons working as The Brindlewood Orthopaedic Centre

Business cards, letterhead

Colors

Designer to choose colors to be used in the design.

Requirements
Must have
• Late addition.
• Cards letterhead must have logos of
• Corvane Federated Institute of Surgeons
• Meridale Orthopaedic Society
Nice to have
• Back of card to have space for appointment time to be added by hand and some blank space for writing incidental other notes.

```html
<!DOCTYPE html>
<html lang="en">
<head>
<meta charset="utf-8">
<title>The Brindlewood Orthopaedic Centre – Business Card</title>
<link href="https://fonts.googleapis.com/css2?family=Montserrat:wght@400;500&display=swap" rel="stylesheet">
<style>
  :root {
    --backdrop: #d6d6d6;
    --brand-blue: #00aeef;
    --paper: #ffffff;
    --ink: #231f20;
    --rule: #555555;
  }
  * { margin: 0; padding: 0; box-sizing: border-box; }
  html, body {
    width: 1200px; height: 1000px; overflow: hidden;
    background: var(--backdrop);
    font-family: "Montserrat", sans-serif;
  }
  .stage { position: relative; width: 1200px; height: 1000px; }
  .card {
    position: absolute; left: 270px; width: 658px; height: 364px;
    border-radius: 30px;
  }
  .card--front { top: 88px; background: var(--brand-blue); }
  .card--back { top: 527px; background: var(--paper); }

  .wordmark {
    position: absolute; white-space: nowrap; font-weight: 400;
    letter-spacing: -0.6px;
  }
  .card--front .wordmark {
    left: 0; right: 0; top: 156px; text-align: center;
    font-size: 31px; color: var(--paper);
  }
  .card--back .wordmark {
    left: 37px; top: 72px; font-size: 25px; color: var(--brand-blue);
  }

  .social {
    position: absolute; left: 0; right: 0; top: 295px;
    display: flex; justify-content: center; align-items: center; gap: 10px;
    color: var(--paper); font-size: 21px; letter-spacing: 0.3px;
  }
  .social__dot {
    width: 30px; height: 30px; border-radius: 50%; background: var(--paper);
  }

  .holder { position: absolute; left: 36px; top: 245px; color: var(--ink); }
  .holder__name { font-size: 22px; line-height: 28px; }
  .holder__role { font-size: 19px; line-height: 26px; color: #333; }

  .divider {
    position: absolute; left: 315px; top: 212px; width: 1px; height: 115px;
    background: var(--rule);
  }

  .contacts {
    position: absolute; left: 353px; top: 213px; list-style: none;
    color: var(--ink); font-size: 17.5px;
  }
  .contacts li {
    display: flex; align-items: center; gap: 9px; height: 29.5px;
  }
  .contacts svg { width: 26px; height: 26px; flex: none; }
</style>
</head>
<body>
<main class="stage">
  <section class="card card--front" aria-label="Card front">
    <p class="wordmark">The Brindlewood Orthopaedic Centre</p>
    <div class="social">
      <span class="social__dot" aria-hidden="true"></span>
      <span class="social__handle">brw_ortho</span>
    </div>
  </section>

  <section class="card card--back" aria-label="Card back">
    <p class="wordmark">The Brindlewood Orthopaedic Centre</p>

    <div class="holder">
      <p class="holder__name">Name</p>
      <p class="holder__role">Designation</p>
    </div>

    <div class="divider" aria-hidden="true"></div>

    <ul class="contacts">
      <li>
        <svg viewBox="0 0 26 26" aria-hidden="true">
          <circle cx="13" cy="13" r="13" fill="var(--brand-blue)"/>
          <path d="M13 6a5 5 0 0 0-5 5c0 3.8 5 9 5 9s5-5.2 5-9a5 5 0 0 0-5-5z" fill="#fff"/>
          <circle cx="13" cy="11" r="2" fill="var(--brand-blue)"/>
        </svg>
        <span>Address</span>
      </li>
      <li>
        <svg viewBox="0 0 26 26" aria-hidden="true">
          <circle cx="13" cy="13" r="13" fill="var(--brand-blue)"/>
          <path d="M9 6.5l2.3 3.3-1.4 1.6c.9 1.9 2.3 3.4 4.2 4.4l1.6-1.4 3.3 2.3-1 2.4c-5.4-.3-9.8-4.7-10.1-10.1z" fill="#fff"/>
        </svg>
        <span>313-BRW-456</span>
      </li>
      <li>
        <svg viewBox="0 0 26 26" aria-hidden="true">
          <circle cx="13" cy="13" r="13" fill="var(--brand-blue)"/>
          <rect x="6.5" y="8.5" width="13" height="9" rx="1" fill="none" stroke="#fff" stroke-width="1.6"/>
          <path d="M6.8 9l6.2 5 6.2-5" fill="none" stroke="#fff" stroke-width="1.6"/>
        </svg>
        <span>info@brindlewoodortho.com</span>
      </li>
      <li>
        <svg viewBox="0 0 26 26" aria-hidden="true">
          <circle cx="12" cy="12" r="10" fill="none" stroke="var(--brand-blue)" stroke-width="2"/>
          <ellipse cx="12" cy="12" rx="4" ry="10" fill="none" stroke="var(--brand-blue)" stroke-width="1.6"/>
          <path d="M2 12h20M4 7h16M4 17h16" stroke="var(--brand-blue)" stroke-width="1.6"/>
          <path d="M16 15l8 3-3.2 1.2L19.6 23z" fill="var(--brand-blue)" stroke="#fff" stroke-width="0.8"/>
        </svg>
        <span>www.brindlewoodortho.com</span>
      </li>
    </ul>
  </section>
</main>
</body>
</html>
```